Trucking company needs business card design

New trucking company needs fresh ideas on a business card. Contracted exclusively to ParcelWing, can incorporate their colors or style, but not necessary.
Calder Haulage, Inc (with or without the Inc.)
Dale Whitcombe, CEO
801-555-0147
PO BOX 372
Kestrel, UT
Updates

Need to add my email address to the card--calderhaulageinc@roadmail.example

Industry/Entity Type

Trucking Company

```html
<!DOCTYPE html>
<html lang="en">
<head>
<meta charset="utf-8">
<title>Calder Haulage, Inc — Business Card</title>
<link rel="stylesheet" href="https://fonts.googleapis.com/css2?family=Aldrich&family=Josefin+Sans:wght@400&family=Open+Sans:wght@700&display=swap">
<style>
  :root {
    --canvas-bg: #e9e4dd;
    --card-red: #fb2a2a;
    --ink-dark: #1c0404;
    --ink-contact: #2e0707;
    --white: #ffffff;
    --back-top: #f32a2a;
    --back-mid: #7a0606;
    --back-bottom: #3b0000;
    --title-silver: #cfcfcf;
    --shadow: rgba(0, 0, 0, 0.35);
  }
  html, body {
    margin: 0;
    padding: 0;
    width: 1200px;
    height: 1000px;
    overflow: hidden;
    background: var(--canvas-bg);
  }
  .canvas {
    position: relative;
    width: 1200px;
    height: 1000px;
  }
  .card {
    position: absolute;
    box-shadow: 6px 8px 14px var(--shadow);
    overflow: hidden;
  }

  /* Front card */
  .card-front {
    left: 40px;
    top: 40px;
    width: 680px;
    height: 400px;
    background: var(--card-red);
  }
  .company-name {
    position: absolute;
    left: 15px;
    top: 22px;
    margin: 0;
    font-family: "Open Sans", sans-serif;
    font-weight: 700;
    font-size: 20px;
    color: var(--white);
    letter-spacing: 0.3px;
  }
  .truck-photo-front {
    position: absolute;
    left: 5px;
    top: 105px;
    width: 290px;
    height: 310px;
    background: linear-gradient(180deg, #ff6b6b 0%, #f23c3c 45%, #c81a1a 100%);
  }
  .person-name {
    position: absolute;
    left: 322px;
    top: 128px;
    margin: 0;
    font-family: "Aldrich", sans-serif;
    font-weight: 400;
    font-size: 31px;
    color: var(--ink-dark);
    letter-spacing: 1.5px;
    white-space: nowrap;
  }
  .title-rule {
    position: absolute;
    left: 325px;
    top: 178px;
    width: 232px;
    height: 3px;
    background: var(--white);
  }
  .person-role {
    position: absolute;
    left: 567px;
    top: 162px;
    margin: 0;
    font-family: "Aldrich", sans-serif;
    font-size: 22px;
    color: var(--white);
    letter-spacing: 1px;
  }
  .contact-list {
    position: absolute;
    left: 328px;
    top: 238px;
    margin: 0;
    padding: 0;
    list-style: none;
    font-family: "Josefin Sans", sans-serif;
    font-size: 15px;
    line-height: 20px;
    letter-spacing: 0.4px;
    color: var(--ink-contact);
    white-space: nowrap;
  }
  .contact-label {
    display: inline-block;
    width: 60px;
  }

  /* Back card */
  .card-back {
    left: 490px;
    top: 540px;
    width: 630px;
    height: 380px;
    background: linear-gradient(180deg, var(--back-top) 0%, var(--back-mid) 38%, var(--back-bottom) 62%, var(--back-bottom) 100%);
  }
  .brand-title {
    position: absolute;
    left: 0;
    right: 0;
    top: 48px;
    margin: 0;
    text-align: center;
    font-family: "Aldrich", sans-serif;
    font-weight: 400;
    font-size: 34px;
    letter-spacing: 3px;
    color: var(--title-silver);
    white-space: nowrap;
  }
  .truck-photo-back {
    position: absolute;
    left: 170px;
    top: 140px;
    width: 460px;
    height: 235px;
    background: linear-gradient(160deg, #7a1010 0%, #a01818 40%, #4a0303 100%);
  }
</style>
</head>
<body>
<main class="canvas">
  <section class="card card-front" aria-label="Business card front">
    <h2 class="company-name">Calder Haulage, Inc</h2>
    <div class="truck-photo-front" role="img" aria-label="Photo of a semi truck cab seen from the front, tinted red"></div>
    <h1 class="person-name">DALE WHITCOMBE</h1>
    <div class="title-rule"></div>
    <p class="person-role">CEO</p>
    <ul class="contact-list">
      <li>PO BOX 372</li>
      <li>Kestrel, UT</li>
      <li><span class="contact-label">Phone</span>: 801-555-0147</li>
      <li><span class="contact-label">Email</span>: calderhaulageinc@roadmail.example</li>
    </ul>
  </section>

  <section class="card card-back" aria-label="Business card back">
    <h2 class="brand-title">CALDER HAULAGE, INC</h2>
    <div class="truck-photo-back" role="img" aria-label="Photo of a red semi truck with a white trailer, angled view"></div>
  </section>
</main>
</body>
</html>
```